Taro Velmund Website

I have a client who is a physical therapist who I am redeveloping a website for. The new site will be a combination of two sites, once that handles the practice site of the business and another for the education side of the business in which they will accept online registration for therapeutic training courses for physical therapy students.

The existing sites (just for background purposes) are here:

Private Practice: http://brivantelinc.com/
Education: http://doltrafoundation.com/

So, the new site will be a modern looking site that combines both the private practice content and the education content (register for classes) information.

The home page should have a clear distinction between private practice and education. I am thinking that a button or icon to view/register for classes somewhere on the Home page would lead users to that section of the website that deals specifically with education.

So, that said, I am think the navigation should include the following:

Home
About Us
Our Services
Education
Contact Us

The client has provided the following websites as examples sites in which they like the colors. Here is the direct quote from the client:

"We were looking for sites that looked comfortable in colors and presentation, please view so you have a better idea what we want the feel and colors to be like

http://www.pikowestrips.com/

http://www.marnefield.com/

www.zelquabeam.com"

Note that all examples they provided have a similar type of layout with a large slideshow image front and center, horizontal navigation and large footer areas with contact information and links to pages and social networks.

I am also going to be working on a logo for them, I have yet to decide on what text that will include or what icons (if any) will be a part of that. I am thinking that the doctor's name "Taro Velmund" but I am still struggling with that so a placeholder logo for now would be fine.

```html
<!DOCTYPE html>
<html lang="en">
<head>
<meta charset="utf-8">
<title>Brivantel – About Us</title>
<link href="https://fonts.googleapis.com/css2?family=Raleway:wght@500;600;700&family=Arimo:wght@400;700&display=swap" rel="stylesheet">
<style>
:root{
  --green:#0d9b5a;
  --text:#444;
  --rule:#dcdcdc;
  --side:#ebebeb;
  --foot:#474747;
  --foot-dark:#393939;
  --foot-text:#b4b4b4;
  --white:#fff;
}
*{margin:0;padding:0;box-sizing:border-box}
html,body{width:1157px;height:1200px;overflow:hidden;background:var(--white)}
body{position:relative;font-family:"Arimo",Arial,sans-serif;color:var(--text)}
.abs{position:absolute}

/* header */
.site-header{position:absolute;left:0;top:0;width:1157px;height:77px;border-bottom:1px solid var(--rule)}
.brand{position:absolute;left:168px;top:16px;display:flex;align-items:center;gap:8px}
.brand-dot{width:36px;height:36px;border-radius:50%;background:var(--green)}
.brand-name{font-family:"Raleway",sans-serif;font-weight:700;font-size:26px;color:var(--green);letter-spacing:-.3px}
.main-nav a{position:absolute;top:33px;font-size:11.5px;color:#666;text-decoration:none}
.main-nav a.active{color:var(--green)}

/* main column */
.photo{position:absolute;left:166px;width:551px}
.section-title{position:absolute;left:167px;font-family:"Raleway",sans-serif;font-weight:600;font-size:16.5px;color:var(--green)}
.copy{position:absolute;left:166px;width:551px;font-size:10.2px;line-height:19px;color:var(--text)}

/* sidebar */
.sidebar{position:absolute;left:750px;top:78px;width:243px;height:881px;background:var(--side)}
.sidebar-title{position:absolute;left:24px;top:27px;font-family:"Raleway",sans-serif;font-weight:600;font-size:17px;color:var(--green)}
.service-photo{position:absolute;left:19px;width:207px;height:127px}
.service-title{position:absolute;left:20px;font-family:"Raleway",sans-serif;font-weight:700;font-size:12.3px;color:var(--green)}
.service-copy{position:absolute;left:21px;width:205px;font-size:9.9px;line-height:19px;color:#555}
.btn{position:absolute;display:block;width:91px;height:27px;line-height:27px;text-align:center;background:var(--green);color:var(--white);font-family:"Raleway",sans-serif;font-weight:600;font-size:9.5px;border-radius:2px;text-decoration:none}

/* footer */
.site-footer{position:absolute;left:0;top:959px;width:1157px;height:193px;background:var(--foot)}
.footer-title{position:absolute;left:167px;top:32px;font-family:"Raleway",sans-serif;font-weight:600;font-size:12.5px;color:var(--white)}
.footer-about{position:absolute;left:167px;top:60px;width:260px;font-size:9.9px;line-height:20px;color:var(--foot-text)}
.footer-links a{position:absolute;left:489px;font-size:9px;color:#ccc;text-decoration:none}
.contact{position:absolute;left:646px;font-size:9px;color:#ccc}
.contact strong{font-weight:700}
.contact-icon{position:absolute;left:647px;width:12px;height:12px}
.social{position:absolute;left:857px;display:flex;align-items:center;gap:7px;font-size:9px;color:#ccc}
.social i{display:block;width:20px;height:20px;border-radius:50%;background:#5c5c5c}
.legal{position:absolute;left:0;top:1152px;width:1157px;height:48px;background:var(--foot-dark);text-align:center;line-height:46px;font-size:10px;color:var(--foot-text)}
</style>
</head>
<body>

<header class="site-header">
  <div class="brand"><span class="brand-dot"></span><span class="brand-name">Brivantel</span></div>
  <nav class="main-nav">
    <a href="#" style="left:543px">Home</a>
    <a href="#" class="active" style="left:622px">About Us</a>
    <a href="#" style="left:718px">Our Services</a>
    <a href="#" style="left:833px">Education</a>
    <a href="#" style="left:932px">Contact Us</a>
  </nav>
</header>

<main>
  <div class="photo" role="img" aria-label="Therapist stretching a patient's arm in a bright clinic" style="top:107px;height:200px;background:linear-gradient(90deg,#e4e4e4,#d9d3cd 45%,#bdbab6 75%,#e9e9e9)"></div>
  <h2 class="section-title" style="top:331px">ABOUT US</h2>
  <p class="copy" style="top:363px">For nearly twenty years, BRIVANTEL, Inc. has offered a unique fusion of expertise, compassion and therapeutic care for a wide variety of patients and clients. From somatic therapy and massage therapy to athletic managment and rehabilitation to personal fitness training, we take a highly effective, hands-on approach to everything we do.For nearly twenty years, BRIVAN-TEL, Inc. has offered a unique fusion of expertise, compassion and therapeutic care for a wide variety of patients and clients. From somatic therapy and massage therapy to athletic managment and rehabilitation to personal fitness training.</p>
  <p class="copy" style="top:477px">we take a highly effective, hands-on approach to everything we do.For nearly twenty years, BRIVANTEL, Inc. has offered a unique fusion of expertise, compassion and therapeutic care for a wide variety of patients and clients. From somatic therapy and massage therapy to athletic managment and rehabilitation to personal fitness training, we take a highly effective, hands-on approach to everything we do.</p>

  <div class="photo" role="img" aria-label="Therapist guiding a patient's shoulders during a stretching exercise" style="top:581px;height:175px;background:linear-gradient(90deg,#eef0ec,#e8ddd4 45%,#b5aea8 80%,#9f9a96)"></div>
  <h2 class="section-title" style="top:779px">COME TO BRIVANTEL AND DISCOVER</h2>
  <p class="copy" style="top:812px">For nearly twenty years, BRIVANTEL, Inc. has offered a unique fusion of expertise, compassion and therapeutic care for a wide variety of patients and clients. From somatic therapy and massage therapy to athletic managment and rehabilitation to personal fitness training, we take a highly effective, hands-on approach to everything we do.For nearly twenty years, BRIVAN-TEL, Inc. has offered a unique fusion of expertise, compassion and therapeutic care for a wide variety of patients and clients. From somatic therapy and massage therapy to athletic managment and rehabilitation to personal fitness training.</p>
</main>

<aside class="sidebar">
  <h2 class="sidebar-title">SERVICES</h2>
  <div class="service-photo" role="img" aria-label="Client receiving a gentle head treatment" style="top:62px;background:linear-gradient(135deg,#d9a48e,#e8c0ae 50%,#b58c9a)"></div>
  <h3 class="service-title" style="top:209px">SOMATIC THERAPY</h3>
  <p class="service-copy" style="top:233px">Whether your goal is relaxation, pain relief or soft-tissue healing and repair, massage therapy offers exponential benefits, and is an excellent companion therapy...</p>
  <a class="btn" href="#" style="left:19px;top:319px">READ MORE</a>

  <div class="service-photo" role="img" aria-label="Hands giving a back massage" style="top:377px;background:linear-gradient(160deg,#f6e2c4,#e8b98a 55%,#d99f6c)"></div>
  <h3 class="service-title" style="top:523px">MASSAGE THERAPY</h3>
  <p class="service-copy" style="top:547px">Whether your goal is relaxation, pain relief or soft-tissue healing and repair, massage therapy offers exponential benefits, and is an excellent companion therapy...</p>
  <a class="btn" href="#" style="left:19px;top:633px">READ MORE</a>
</aside>

<footer class="site-footer">
  <h3 class="footer-title">WHO WE ARE</h3>
  <p class="footer-about">At BRIVANTEL, Inc., we firmly believe that you know your body better than anyone else and everything we do springs from that philosophy.</p>
  <a class="btn" href="#" style="left:166px;top:129px">READ MORE</a>

  <nav class="footer-links">
    <a href="#" style="top:41px">Home</a>
    <a href="#" style="top:62px">About Us</a>
    <a href="#" style="top:83px">Our Services</a>
    <a href="#" style="top:104px">Education</a>
    <a href="#" style="top:125px">Contact Us</a>
  </nav>

  <div class="contact" style="top:41px"><strong>Brivantel</strong></div>
  <div class="contact" style="top:62px">Ridgecove, CA 90410</div>
  <svg class="contact-icon" style="top:87px" viewBox="0 0 12 12"><path d="M2.5 1l2 2.2-1 1.3c.6 1.5 1.6 2.5 3 3.1l1.3-1 2.2 2-.9 1.9C5 10.3 1.7 7 .8 2z" fill="#ccc"/></svg>
  <div class="contact" style="top:87px;left:666px">(555) 014-2286</div>
  <svg class="contact-icon" style="top:112px" viewBox="0 0 12 12"><rect x="3" y="1" width="6" height="3" fill="#ccc"/><rect x="1" y="4.5" width="10" height="4.5" rx="1" fill="#ccc"/><rect x="3" y="8" width="6" height="3" fill="#ccc"/></svg>
  <div class="contact" style="top:112px;left:666px">(555) 014-2290</div>
  <svg class="contact-icon" style="top:134px" viewBox="0 0 12 12"><rect x="1" y="2.5" width="10" height="7" fill="none" stroke="#ccc"/><path d="M1 2.5l5 4 5-4" fill="none" stroke="#ccc"/></svg>
  <div class="contact" style="top:134px;left:666px">office@brivantelmail.net</div>

  <div class="social" style="top:38px"><i></i>: Circlebook</div>
  <div class="social" style="top:67px"><i></i>: Workline</div>
  <div class="social" style="top:96px"><i></i>: Orbitplus</div>
  <div class="social" style="top:126px"><i></i>: Viewtube</div>
</footer>

<div class="legal">Copyrights &nbsp;@2014. Brivantel. All Rights Reserved</div>

</body>
</html>
```